Use Existing Logo to Design Letterhead, Envelope and Presentation Folder

We are a storm shelter company based out of Oklahoma City. We have an existing logo and brand image. We are looking for professionally designed letterhead, mailing envelopes and folders using our brand guidelines (attached). The font to be used is Futura.

The image represents simple professionalism.
We compete on quality, not price.
We value attention to detail and craftsmanship in our work.
The colors and layout are bold and clean.

Again, this is for:
1) Letterhead - contains name, address, phone, fax, and website address
2) Envelopes - logo, tagline and return address
3) Presentation Folders - logo and tag line

Our tag line is:
"America's Best EF5 Rated Storm Shelters and Family Safety Products"

Please submit your designs and once we have the initial layouts, we will provide the top designers with our contact information.

Good luck!

```html
<!DOCTYPE html>
<html lang="en">
<head>
<meta charset="utf-8">
<title>Steadfast Havens – Stationery and Presentation Set</title>
<link rel="stylesheet" href="https://fonts.googleapis.com/css2?family=Jost:wght@400;500&family=PT+Sans+Narrow:wght@400;700&family=PT+Sans:ital@0;1&display=swap">
<style>
  :root {
    --brand-blue: #1c2fa0;
    --brand-blue-deep: #15257f;
    --charcoal: #5e5f63;
    --mid-grey: #a9aaad;
    --light-grey: #e4e4e6;
    --paper: #ffffff;
    --pale-lavender: #d3d7ef;
    --text-dark: #3c3c40;
    --wordmark-pale: #d9dbe4;
  }
  * { box-sizing: border-box; margin: 0; padding: 0; }
  html, body { width: 1200px; height: 960px; overflow: hidden; background: var(--paper); }
  .canvas { position: relative; width: 1200px; height: 960px; font-family: "Jost", "Futura", sans-serif; }

  .sheet { position: absolute; overflow: hidden; background: var(--paper); }
  .sheet svg.backdrop { position: absolute; inset: 0; width: 100%; height: 100%; }

  .wordmark { position: absolute; font-family: "Jost", sans-serif; font-weight: 400; line-height: 1; color: var(--charcoal); }
  .wordmark span { display: block; }

  /* Folder */
  .folder { left: 30px; top: 35px; width: 325px; height: 450px; border: 1px solid #eee; }
  .folder .wordmark { left: 56px; top: 180px; color: var(--wordmark-pale); text-align: center; width: 215px; }
  .folder .wordmark .line-one { font-size: 40px; letter-spacing: -0.5px; }
  .folder .wordmark .line-two { font-size: 20px; letter-spacing: 11px; margin-top: 6px; padding-left: 8px; }
  .folder .web { position: absolute; left: 204px; top: 411px; font-size: 8px; color: #e8e8ea; font-family: "PT Sans", sans-serif; }
  .folder .web b { color: #9fd0ff; font-weight: 700; }

  /* Letterhead */
  .letterhead { left: 368px; top: 35px; width: 347px; height: 450px; border: 1px solid #eee; }
  .letterhead .wordmark { left: 20px; top: 64px; color: var(--brand-blue); }
  .letterhead .wordmark .line-one { font-size: 15px; }
  .letterhead .wordmark .line-two { font-size: 8px; letter-spacing: 3.6px; margin-top: 2px; }
  .contact-strip { position: absolute; left: 118px; top: 40px; display: flex; gap: 5px; font-family: "PT Sans", sans-serif; font-size: 5.5px; line-height: 1.25; color: var(--text-dark); }
  .contact-strip div + div { border-left: 1px solid #999; padding-left: 5px; }

  /* Envelope */
  .envelope { left: 741px; top: 268px; width: 430px; height: 217px; border: 1px solid #ddd; }
  .envelope .wordmark { left: 317px; top: 63px; color: var(--charcoal); }
  .envelope .wordmark .line-one { font-size: 17px; }
  .envelope .wordmark .line-two { font-size: 9px; letter-spacing: 3.5px; margin-top: 2px; color: var(--brand-blue); }
  .return-address { position: absolute; left: 14px; top: 18px; width: 230px; font-family: "PT Sans", sans-serif; font-size: 5.5px; color: var(--text-dark); }
  .return-address .row { border-top: 1px solid #777; padding: 3px 29px 4px; line-height: 1.2; }
  .return-address .row:last-child { border-bottom: 1px solid #777; }
  .return-address .web { padding: 9px 29px 0; font-size: 9px; }
  .return-address .web b { color: var(--brand-blue); }

  /* Slides */
  .slide { top: 502px; width: 565px; height: 423px; }
  .slide-cover { left: 30px; }
  .slide-content { left: 606px; }
  .slide .heading { position: absolute; font-family: "PT Sans Narrow", sans-serif; font-weight: 700; color: #e8e9f6; }
  .slide-cover .heading { left: 29px; top: 56px; font-size: 32px; }
  .slide-cover .subtext { position: absolute; left: 29px; top: 100px; width: 360px; font-family: "PT Sans Narrow", sans-serif; font-size: 14px; line-height: 1.45; color: #dfe2f4; }
  .slide-cover .wordmark { left: 369px; top: 346px; color: var(--charcoal); }
  .slide-cover .wordmark .line-one { font-size: 32px; }
  .slide-cover .wordmark .line-two { font-size: 15px; letter-spacing: 7.5px; margin-top: 3px; color: var(--brand-blue); }

  .slide-content .heading { left: 0; width: 100%; top: 8px; text-align: center; font-size: 20px; color: #fff; }
  .slide-content .wordmark { left: 436px; top: 334px; color: var(--charcoal); }
  .slide-content .wordmark .line-one { font-size: 20px; }
  .slide-content .wordmark .line-two { font-size: 10px; letter-spacing: 4.5px; margin-top: 2px; color: var(--brand-blue); }
  .timeline-note { position: absolute; left: 19px; top: 394px; font-family: "PT Sans", sans-serif; font-style: italic; font-size: 12px; color: #fff; }
  .nav-button { position: absolute; top: 391px; height: 24px; padding: 0 10px; border-radius: 5px; background: #0d1a5e; color: #fff; font-family: "PT Sans", sans-serif; font-size: 12px; line-height: 24px; }
  .nav-back { left: 451px; }
  .nav-next { left: 505px; }
</style>
</head>
<body>
<main class="canvas">

  <section class="sheet folder" aria-label="Presentation folder">
    <svg class="backdrop" viewBox="0 0 325 450" aria-hidden="true">
      <path d="M0 315 Q110 300 190 340 L190 450 L0 450Z" fill="var(--light-grey)"/>
      <path d="M0 350 Q90 332 170 360 L170 450 L0 450Z" fill="var(--charcoal)"/>
      <circle cx="300" cy="470" r="195" fill="var(--brand-blue)"/>
      <circle cx="320" cy="490" r="150" fill="var(--charcoal)"/>
      <path d="M195 355 Q270 345 325 375 L325 380 Q270 355 205 362Z" fill="var(--paper)"/>
      <circle cx="70" cy="440" r="55" fill="none" stroke="#6e6f73" stroke-width="18"/>
    </svg>
    <div class="wordmark"><span class="line-one">STEADFAST</span><span class="line-two">HAVENS</span></div>
    <div class="web">www.<b>companyname</b>.com</div>
  </section>

  <section class="sheet letterhead" aria-label="Letterhead">
    <svg class="backdrop" viewBox="0 0 347 450" aria-hidden="true">
      <defs>
        <linearGradient id="lh-sweep" x1="0" x2="1" y1="0" y2="0">
          <stop offset="0" stop-color="#fff"/><stop offset="1" stop-color="#c9c9cc"/>
        </linearGradient>
      </defs>
      <path d="M60 0 Q200 80 347 20 L347 0Z" fill="url(#lh-sweep)"/>
      <path d="M160 0 Q260 60 347 45 L347 30 Q260 40 200 0Z" fill="#ececee"/>
      <path d="M0 420 Q170 405 347 428 L347 450 L0 450Z" fill="var(--charcoal)"/>
      <path d="M0 420 Q170 405 347 428 L347 438 Q170 420 0 428Z" fill="var(--brand-blue)"/>
      <path d="M0 416 Q170 400 347 424 L347 428 Q170 405 0 420Z" fill="var(--light-grey)"/>
    </svg>
    <div class="wordmark"><span class="line-one">STEADFAST</span><span class="line-two">HAVENS</span></div>
    <div class="contact-strip">
      <div>Street No.0000 (somewhere),<br><b>City, State - Country.</b></div>
      <div>Tel : +000 11 000000<br>Mobile: 0000 1111</div>
      <div>info@<b>companyname</b>.com<br>www.<b>companyname</b>.com</div>
    </div>
  </section>

  <section class="sheet envelope" aria-label="Envelope">
    <svg class="backdrop" viewBox="0 0 430 217" aria-hidden="true">
      <defs>
        <linearGradient id="env-sweep" x1="0" x2="1" y1="0" y2="1">
          <stop offset="0" stop-color="#cfcfd2"/><stop offset="1" stop-color="#fff"/>
        </linearGradient>
      </defs>
      <path d="M0 217 Q40 60 130 0 L0 0Z" fill="url(#env-sweep)" opacity="0.7"/>
      <path d="M0 217 Q70 90 200 40 Q90 110 40 217Z" fill="#e9e9eb"/>
    </svg>
    <div class="return-address">
      <div class="row">Street No.0000 (somewhere),<br><b>City, State - Country.</b></div>
      <div class="row">Tel : +000 11 000000<br>Mobile: 0000 1111</div>
      <div class="row">info@<b>companyname</b>.com</div>
      <div class="web">www.<b>companyname</b>.com</div>
    </div>
    <div class="wordmark"><span class="line-one">STEADFAST</span><span class="line-two">HAVENS</span></div>
  </section>

  <section class="sheet slide slide-cover" aria-label="Presentation cover slide">
    <svg class="backdrop" viewBox="0 0 565 423" aria-hidden="true">
      <rect width="565" height="423" fill="var(--brand-blue)"/>
      <path d="M120 423 L268 226 L340 268 L565 0 L565 423Z" fill="#f1f1f2"/>
      <path d="M148 423 L282 246 L352 287 L565 28 L565 423Z" fill="#b8b9bc"/>
    </svg>
    <h1 class="heading">Project Title Here</h1>
    <p class="subtext">Subtext here Subtext here Subtext here Subtext here Subtext here Subtext here Subtext here Subtext here</p>
    <div class="wordmark"><span class="line-one">STEADFAST</span><span class="line-two">HAVENS</span></div>
  </section>

  <section class="sheet slide slide-content" aria-label="Presentation content slide">
    <svg class="backdrop" viewBox="0 0 565 423" aria-hidden="true">
      <defs>
        <linearGradient id="sc-field" x1="0" x2="0" y1="0" y2="1">
          <stop offset="0" stop-color="#e4e6f4"/><stop offset="1" stop-color="var(--pale-lavender)"/>
        </linearGradient>
        <linearGradient id="sc-bar" x1="0" x2="0" y1="0" y2="1">
          <stop offset="0" stop-color="#2a3eb8"/><stop offset="1" stop-color="var(--brand-blue-deep)"/>
        </linearGradient>
      </defs>
      <rect width="565" height="423" fill="url(#sc-field)"/>
      <path d="M135 380 L258 226 L325 268 L515 42 L565 42 L565 380Z" fill="#fbfbfb"/>
      <path d="M160 380 L268 246 L336 288 L528 60 L565 60 L565 380Z" fill="#ececed"/>
      <rect width="565" height="42" fill="url(#sc-bar)"/>
      <rect y="380" width="565" height="43" fill="url(#sc-bar)"/>
      <rect y="42" width="565" height="2" fill="#9aa3d8"/>
    </svg>
    <h2 class="heading">Slide Title</h2>
    <div class="wordmark"><span class="line-one">STEADFAST</span><span class="line-two">HAVENS</span></div>
    <p class="timeline-note">Timeline about your Slide Presentation</p>
    <span class="nav-button nav-back">Back</span>
    <span class="nav-button nav-next">Next</span>
  </section>

</main>
</body>
</html>
```